Brightmoor Machinery Forklift rental website

I'm seeking a proficient web developer to build a forklift rental website tailored to large warehouses. I am not looking for a generic site, I want it to be attractive and sleek to potential customers. I have attached my logo to give a better idea about my design preferences .
The site must encompass various functionalities: - A rental booking system to allow customers reserve forklifts seamlessly, making the rental process simpler. - An inventory management system that offers real-time tracking of our diverse range of forklifts including Electric forklifts, Reach trucks, Order pickers, Sit and Stand up counterbalances, Swing reach, Propane sit down counterbalances and chargers. For each forklift listed, the site should display explicit specifications, current rental rates, and an availability calendar to aid customers in making informed rental decisions. Ideal skills for this role will include web development, experience in building booking and potentially some knowledge of the renting industry, although this is not essential. Experience in creating inventory management systems is also looked upon favorably. I would also like a section that I can list forklifts for sale. Preferably the website would be designed to convert into an app as well. The website will need a payment portal that can accept credit cards, ach payments and possibly e-check/ wire transfer.
Most bookings will be monthly so I need a system that can accommodate that. I will also need an option to leave the bookings open ended in the event the customer wants to keep the unit until further notice.
Target Market(s)
Industrial warehouses
Coding
Coded - Design and coding required
Number of Pages Required
1 page
Look and feel
Each slider illustrates characteristics of the customer's brand and the style your logo design should communicate.

```html
<!DOCTYPE html>
<html lang="en">
<head>
<meta charset="utf-8">
<title>Brightmoor Machinery – Forklift Rentals</title>
<link href="https://fonts.googleapis.com/css2?family=Orbitron:wght@700;900&family=Roboto:wght@400;500;700&display=swap" rel="stylesheet">
<style>
:root{
  --red:#e31e24;
  --navy:#233a7f;
  --ink:#111111;
  --black:#0a0a0a;
  --grey-bg:#f3f3f3;
  --text:#555555;
  --white:#ffffff;
}
*{box-sizing:border-box;margin:0;padding:0}
html,body{width:1200px;height:4666px;overflow:hidden}
body{position:relative;font-family:'Roboto',sans-serif;color:var(--ink);background:var(--white)}
.abs{position:absolute}
.display{font-family:'Orbitron',sans-serif;font-weight:900;text-transform:uppercase;letter-spacing:1px}
.accent{color:var(--red)}
.btn{position:absolute;display:flex;align-items:center;justify-content:center;font-size:14px;font-weight:500;text-transform:uppercase;border:2px solid var(--red);color:var(--navy);background:var(--white)}
.btn.solid{background:var(--red);color:var(--white)}
.photo{position:absolute}

/* header */
.site-header{position:absolute;left:0;top:0;width:1200px;height:107px;background:var(--white)}
.brand{position:absolute;display:flex;align-items:center;gap:10px;font-weight:700;text-transform:uppercase}
.brand .mark{width:22px;height:22px;background:var(--red)}
.call-panel{position:absolute;right:0;top:0}
.nav-bar{position:absolute;left:0;top:107px;width:1200px;height:47px;background:var(--black)}
.nav-bar a{position:absolute;top:16px;color:var(--white);font-size:13px;font-weight:700;text-decoration:none}
.nav-bar a.active{color:var(--red);text-decoration:underline}
.social-sq{position:absolute;top:0;width:37px;height:47px;display:flex;align-items:center;justify-content:center;color:var(--white);font-size:10px;font-weight:500}

/* hero */
.hero-title{position:absolute;right:112px;top:318px;text-align:right;color:var(--white);font-size:46px;line-height:56px}
.hero-copy{position:absolute;right:112px;top:446px;width:480px;text-align:right;color:var(--white);font-size:20px;line-height:31px}

/* about */
.section-title{font-size:40px}
.para{font-size:14.5px;line-height:25.5px;color:var(--text);text-align:justify}

/* forklifts */
.card-img{position:absolute;background:var(--white);box-shadow:0 0 8px rgba(0,0,0,.15);padding:6px}
.card-img div{width:100%;height:100%}
.card-title{position:absolute;font-size:19px;font-weight:500;text-transform:uppercase}
.card-text{position:absolute;font-size:14px;line-height:24px;color:var(--text);width:410px}
.rate{position:absolute;display:flex;align-items:center;gap:14px;font-size:13.5px;font-weight:500;text-transform:uppercase;color:var(--ink)}
.rate b{color:var(--navy)}
.box{width:12px;height:12px;border:1.5px solid var(--red)}
.arrow{position:absolute;width:34px;height:34px;border-radius:50%;display:flex;align-items:center;justify-content:center}

/* sale */
.check-list{position:absolute;list-style:none}
.check-list li{display:flex;align-items:center;gap:24px;height:32.6px;font-size:16px;color:var(--ink)}

/* why */
.feature{position:absolute;top:3332px;width:306px;height:342px;background:var(--white);text-align:center}
.feature .icon{width:88px;height:88px;border-radius:50%;background:var(--red);margin:34px auto 0;display:flex;align-items:center;justify-content:center}
.feature h3{margin-top:26px;font-size:17px;font-weight:500;text-transform:uppercase}
.feature p{margin:22px 26px 0;font-size:14px;line-height:25px;color:var(--text)}

/* contact */
.field{position:absolute;background:var(--white);box-shadow:0 2px 8px rgba(0,0,0,.12);font-size:14px;color:#444;padding:16px 18px}

/* footer */
.footer-head{position:absolute;top:4348px;color:var(--white);font-size:18px;font-weight:500}
.footer-list{position:absolute;top:4397px;list-style:none}
.footer-list li{height:36px;color:var(--white);font-size:13.5px}
.contact-block{position:absolute;left:873px;top:4397px;color:var(--white);width:215px}
.contact-block h4{font-size:16px;font-weight:500;margin-bottom:6px}
.contact-block p{font-size:11.5px;line-height:17px;margin-bottom:14px}
.round{width:28px;height:28px;border-radius:50%;border:1.5px solid var(--white);color:var(--white);font-size:8px;display:flex;align-items:center;justify-content:center}
.copyright-bar{position:absolute;left:0;top:4600px;width:1200px;height:66px;background:var(--red)}
.pay{position:absolute;top:22px;width:42px;height:24px;background:var(--white);border-radius:3px;font-size:8px;font-weight:700;color:var(--navy);display:flex;align-items:center;justify-content:center}
</style>
</head>
<body>

<!-- Header -->
<header class="site-header">
  <div class="brand" style="left:112px;top:36px;font-size:19px;color:var(--ink)"><span class="mark"></span>Brightmoor Machinery</div>
  <div class="btn solid" style="left:715px;top:31px;width:165px;height:47px;font-size:13px">Request a Quote</div>
  <svg class="call-panel" width="270" height="170" viewBox="0 0 270 170"><polygon points="100,0 270,0 270,170 0,170" fill="#233a7f"/></svg>
  <div class="abs" style="left:1022px;top:36px;width:40px;height:40px;border-radius:50%;background:var(--white);display:flex;align-items:center;justify-content:center">
    <svg width="18" height="18" viewBox="0 0 24 24"><path d="M6.6 10.8a15 15 0 0 0 6.6 6.6l2.2-2.2a1 1 0 0 1 1-.25 11.4 11.4 0 0 0 3.6.57 1 1 0 0 1 1 1V20a1 1 0 0 1-1 1A17 17 0 0 1 3 4a1 1 0 0 1 1-1h3.5a1 1 0 0 1 1 1c0 1.25.2 2.45.57 3.57a1 1 0 0 1-.25 1z" fill="#e31e24"/></svg>
  </div>
  <div class="abs" style="left:1077px;top:48px;color:var(--white);font-size:11px;font-weight:500">CALL US TODAY!</div>
</header>
<div class="abs" style="left:967px;top:90px;color:var(--white);font-size:22px;font-weight:500;z-index:3">+1 (555) 014 2290</div>

<nav class="nav-bar">
  <a class="active" style="left:110px">HOME</a>
  <a style="left:194px">ABOUT US</a>
  <a style="left:303px">FORKLIFT LISTS</a>
  <a style="left:450px">PRICING</a>
  <a style="left:548px">CONTACT US</a>
  <div class="social-sq" style="left:745px;background:var(--red)">Feed</div>
  <div class="social-sq" style="left:782px">Pics</div>
  <div class="social-sq" style="left:819px">Post</div>
  <div class="social-sq" style="left:856px">Link</div>
</nav>

<!-- Hero -->
<section>
  <div class="photo" role="img" aria-label="Red and grey electric reach truck parked on a warehouse floor" style="left:0;top:154px;width:1200px;height:686px;background:linear-gradient(110deg,#5a5d5f 0%,#3e4143 45%,#2b2e31 100%)"></div>
  <svg class="abs" style="left:0;top:773px" width="1200" height="67"><polygon points="335,67 410,0 1200,0 1200,67" fill="#fff"/></svg>
  <h1 class="hero-title display">Brightmoor<br>Machinery</h1>
  <p class="hero-copy">Lorem ipsum dolor sit amet, consectetur adipiscing elit, sed do eiusmod tempor incididunt ut labore et dolore magna aliquea.</p>
  <div class="btn solid" style="left:958px;top:560px;width:130px;height:48px;font-size:13px">Rent Now</div>
  <div class="abs" style="left:550px;top:720px;width:100px;height:100px;border-radius:50%;background:var(--white);box-shadow:0 0 10px rgba(0,0,0,.2);display:flex;align-items:center;justify-content:center">
    <svg width="22" height="22" viewBox="0 0 24 24" fill="none" stroke="#233a7f" stroke-width="2.5"><path d="M5 5l7 7 7-7M5 12l7 7 7-7"/></svg>
  </div>
</section>

<!-- About -->
<section>
  <div class="abs" style="left:531px;top:905px;width:557px;height:65px;background:#e9e9e9"></div>
  <div class="photo" role="img" aria-label="Red counterbalance forklift in a warehouse" style="left:642px;top:905px;width:446px;height:470px;background:linear-gradient(160deg,#d9d9d9,#8c8c8c 55%,#555)"></div>
  <h2 class="abs display section-title" style="left:112px;top:1010px">About <span class="accent">Us</span></h2>
  <p class="abs para" style="left:112px;top:1078px;width:468px">Lorem ipsum dolor sit amet, consectetur adipiscing elit, sed do eiusmod tempor incididunt ut labore et dolore magna aliqua. Ut enim ad minim veniam, quis nostrud exercitation ullamco laboris nisi ut aliquip ex ea commodo consequat. Duis aute irure dolor in reprehenderit in voluptate velit essea.</p>
  <p class="abs para" style="left:112px;top:1218px;width:468px">Lorem ipsum dolor sit amet, consectetur adipiscing elit, sed do eiusmod tempor incididunt ut labore et dolore magna aliqua. Ut enim ad minim veniam, quis nostrud.</p>
  <div class="btn" style="left:112px;top:1328px;width:140px;height:46px">Learn More</div>
</section>

<!-- Our forklifts -->
<section>
  <svg class="abs" style="left:0;top:1502px" width="1200" height="860"><polygon points="110,0 1200,0 1200,748 1090,860 0,860 0,108" fill="#f3f3f3"/></svg>
  <h2 class="abs display section-title" style="left:0;width:1200px;text-align:center;top:1580px">Our <span class="accent">Forklifts</span></h2>
  <div class="arrow" style="left:40px;top:1828px;background:var(--white);box-shadow:0 0 6px rgba(0,0,0,.2)"><svg width="12" height="12" viewBox="0 0 12 12"><path d="M8 1L3 6l5 5" stroke="#111" stroke-width="1.8" fill="none"/></svg></div>
  <div class="arrow" style="left:1125px;top:1828px;background:var(--navy)"><svg width="12" height="12" viewBox="0 0 12 12"><path d="M4 1l5 5-5 5" stroke="#fff" stroke-width="1.8" fill="none"/></svg></div>

  <div class="card-img" style="left:112px;top:1665px;width:470px;height:357px"><div role="img" aria-label="Electric forklift beside a charging station" style="background:linear-gradient(180deg,#cfcfcf,#9a9a9a)"></div></div>
  <div class="abs" style="left:154px;top:1975px;width:2px;height:90px;background:var(--red)"></div>
  <div class="card-title" style="left:182px;top:2049px">Electric Forklifts</div>
  <p class="card-text" style="left:153px;top:2083px">Lorem ipsum dolor sit amet, consectetur adipiscing elit sed do eiusmod tempor incididuntea.</p>
  <div class="rate" style="left:153px;top:2147px"><span class="box"></span>We do 1 day rentals &nbsp;- &nbsp;<b>$100</b></div>
  <div class="rate" style="left:153px;top:2180px"><svg width="13" height="13" viewBox="0 0 14 14"><rect x="1" y="2" width="11" height="11" fill="none" stroke="#e31e24" stroke-width="1.5"/><path d="M4 7l3 3 6-8" stroke="#e31e24" stroke-width="1.6" fill="none"/></svg>We do 1 week rentals &nbsp;- &nbsp;<b>$500</b></div>
  <div class="btn" style="left:153px;top:2228px;width:129px;height:44px">Rent Now</div>

  <div class="card-img" style="left:618px;top:1665px;width:470px;height:357px"><div role="img" aria-label="Reach truck in a warehouse aisle" style="background:linear-gradient(180deg,#d2d2d2,#8f8f8f)"></div></div>
  <div class="abs" style="left:660px;top:1975px;width:2px;height:90px;background:var(--red)"></div>
  <div class="card-title" style="left:688px;top:2049px">Reach Trucks</div>
  <p class="card-text" style="left:659px;top:2083px">Lorem ipsum dolor sit amet, consectetur adipiscing elit sed do eiusmod tempor incididuntea.</p>
  <div class="rate" style="left:659px;top:2147px"><span class="box"></span>We do 1 day rentals &nbsp;- &nbsp;<b>$100</b></div>
  <div class="rate" style="left:659px;top:2180px"><svg width="13" height="13" viewBox="0 0 14 14"><rect x="1" y="2" width="11" height="11" fill="none" stroke="#e31e24" stroke-width="1.5"/><path d="M4 7l3 3 6-8" stroke="#e31e24" stroke-width="1.6" fill="none"/></svg>We do 1 week rentals &nbsp;- &nbsp;<b>$500</b></div>
  <div class="btn solid" style="left:659px;top:2228px;width:129px;height:44px">Rent Now</div>
</section>

<!-- For sale -->
<section>
  <div class="photo" role="img" aria-label="Red electric forklift with overhead guard" style="left:112px;top:2494px;width:556px;height:471px;background:linear-gradient(160deg,#cfcfcf,#7d7d7d 60%,#4a4a4a)"></div>
  <div class="abs" style="left:557px;top:2565px;width:112px;height:400px;background:var(--white)"></div>
  <h2 class="abs display" style="left:620px;top:2598px;font-size:36px;line-height:48px">Forklifts<br><span class="accent">For Sale</span></h2>
  <ul class="check-list" style="left:620px;top:2700px">
    <li><svg width="15" height="15" viewBox="0 0 14 14"><rect x="1" y="2" width="11" height="11" fill="none" stroke="#233a7f" stroke-width="1.5"/><path d="M4 7l3 3 6-8" stroke="#233a7f" stroke-width="1.6" fill="none"/></svg>Electric forklifts</li>
    <li><svg width="15" height="15" viewBox="0 0 14 14"><rect x="1" y="2" width="11" height="11" fill="none" stroke="#233a7f" stroke-width="1.5"/><path d="M4 7l3 3 6-8" stroke="#233a7f" stroke-width="1.6" fill="none"/></svg>Reach trucks</li>
    <li><svg width="15" height="15" viewBox="0 0 14 14"><rect x="1" y="2" width="11" height="11" fill="none" stroke="#233a7f" stroke-width="1.5"/><path d="M4 7l3 3 6-8" stroke="#233a7f" stroke-width="1.6" fill="none"/></svg>Order pickers</li>
    <li><svg width="15" height="15" viewBox="0 0 14 14"><rect x="1" y="2" width="11" height="11" fill="none" stroke="#233a7f" stroke-width="1.5"/><path d="M4 7l3 3 6-8" stroke="#233a7f" stroke-width="1.6" fill="none"/></svg>Sit and Stand up counterbalances</li>
    <li><svg width="15" height="15" viewBox="0 0 14 14"><rect x="1" y="2" width="11" height="11" fill="none" stroke="#233a7f" stroke-width="1.5"/><path d="M4 7l3 3 6-8" stroke="#233a7f" stroke-width="1.6" fill="none"/></svg>Swing reach</li>
    <li><svg width="15" height="15" viewBox="0 0 14 14"><rect x="1" y="2" width="11" height="11" fill="none" stroke="#233a7f" stroke-width="1.5"/><path d="M4 7l3 3 6-8" stroke="#233a7f" stroke-width="1.6" fill="none"/></svg>Propane sit down counterbalances and chargers.</li>
  </ul>
  <div class="btn" style="left:620px;top:2920px;width:130px;height:46px">Sale Now</div>
</section>

<!-- Why choose us -->
<section>
  <svg class="abs" style="left:0;top:3100px" width="1200" height="652"><polygon points="0,0 1090,0 1200,100 1200,652 110,652 0,560" fill="#233a7f"/></svg>
  <h2 class="abs display" style="left:0;width:1200px;text-align:center;top:3172px;font-size:38px;color:var(--white)">Why Choose Us?</h2>
  <p class="abs" style="left:150px;width:900px;text-align:center;top:3237px;font-size:17px;line-height:29px;color:var(--white)">Lorem ipsum dolor sit amet, consectetur adipiscing elit, sed do eiusmod tempor incididunt ut labore et dolore magna aliqua. Ut enim ad minim veniam, quis nostrud exercitata.</p>

  <svg class="abs" style="left:112px;top:3332px" width="306" height="342"><polygon points="30,0 306,0 306,312 276,342 0,342 0,30" fill="#fff"/></svg>
  <div class="feature" style="left:112px;background:none">
    <div class="icon"><svg width="40" height="40" viewBox="0 0 24 24" fill="none" stroke="#fff" stroke-width="1.6"><path d="M6 4h12l4 5-10 12L2 9z M2 9h20 M9 4l3 17 3-17"/></svg></div>
    <h3>Lorem Ipsum Dolor</h3>
    <p>Lorem ipsum dolor sit amet, consec tetur adipiscing elit, sed do eiusmod tempor incididunt ut labore et dolore magna aliqua ut enim ad minim veniam, quis nostrudea.</p>
  </div>

  <svg class="abs" style="left:445px;top:3332px" width="309" height="342"><polygon points="30,1.5 279,1.5 307.5,30 307.5,340.5 30,340.5 1.5,312 1.5,30" fill="#fff" stroke="#e31e24" stroke-width="3"/></svg>
  <div class="feature" style="left:446px;background:none">
    <div class="icon"><svg width="40" height="40" viewBox="0 0 24 24" fill="none" stroke="#fff" stroke-width="1.6"><path d="M3 21V9l9-5 9 5v12z M8 21v-8h8v8 M8 16h8"/></svg></div>
    <h3>Lorem Ipsum Dolor</h3>
    <p>Lorem ipsum dolor sit amet, consec tetur adipiscing elit, sed do eiusmod tempor incididunt ut labore et dolore magna aliqua ut enim ad minim veniam, quis nostrudea.</p>
  </div>

  <svg class="abs" style="left:783px;top:3332px" width="306" height="342"><polygon points="0,0 276,0 306,30 306,342 30,342 0,312" fill="#fff"/></svg>
  <div class="feature" style="left:783px;background:none">
    <div class="icon"><svg width="42" height="42" viewBox="0 0 24 24" fill="none" stroke="#fff" stroke-width="1.6"><path d="M2 17V8h6l3 5v4z M11 17h4 M15 4v13h6 M15 8h4v5h-4"/><circle cx="5" cy="18" r="2"/><circle cx="11" cy="18" r="2"/></svg></div>
    <h3>Lorem Ipsum Dolor</h3>
    <p>Lorem ipsum dolor sit amet, consec tetur adipiscing elit, sed do eiusmod tempor incididunt ut labore et dolore magna aliqua ut enim ad minim veniam, quis nostrudea.</p>
  </div>
</section>

<!-- Contact form -->
<section>
  <h2 class="abs display section-title" style="left:0;width:1200px;text-align:center;top:3858px">Get <span class="accent">In Touch</span></h2>
  <div class="field" style="left:165px;top:3937px;width:282px;height:48px">Full Name</div>
  <div class="field" style="left:458px;top:3937px;width:282px;height:48px">Phone</div>
  <div class="field" style="left:751px;top:3937px;width:283px;height:48px">Email Address</div>
  <div class="field" style="left:165px;top:4003px;width:869px;height:90px">Message</div>
  <div class="btn" style="left:520px;top:4110px;width:160px;height:46px;font-size:13px">Send Message</div>
</section>

<!-- Footer -->
<footer>
  <svg class="abs" style="left:0;top:4200px" width="1200" height="400"><polygon points="0,64 790,64 862,0 1200,0 1200,400 0,400" fill="#0a0a0a"/></svg>
  <div class="brand" style="left:112px;top:4418px;font-size:22px;color:var(--white);width:250px;flex-wrap:wrap"><span class="mark"></span>Brightmoor<br>Machinery</div>
  <div class="abs" style="left:170px;top:4506px;display:flex;gap:5px">
    <span class="round">Fd</span><span class="round">Pt</span><span class="round">Pc</span><span class="round">Ln</span>
  </div>

  <div class="footer-head" style="left:455px">Quick Links</div>
  <ul class="footer-list" style="left:455px"><li>Home</li><li>About Us</li><li>Forklift Lists</li><li>Pricing</li><li>Contact Us</li></ul>

  <div class="footer-head" style="left:645px">Support</div>
  <ul class="footer-list" style="left:645px"><li>Privacy Policy</li><li>Terms And Conditions</li><li>Legal Support</li><li>Sitemap</li></ul>

  <div class="footer-head" style="left:873px">Contact Info</div>
  <div class="contact-block">
    <h4>Address:</h4><p>465, Lorumipsum Dolore Sed Amet,<br>United States</p>
    <h4>Phone:</h4><p>+1 (555) 014 2290</p>
    <h4>Email:</h4><p>info@brightmoormachinery.com</p>
  </div>

  <div class="copyright-bar">
    <div class="abs" style="left:0;width:1200px;text-align:center;top:24px;color:var(--white);font-size:13.5px">© 2024 BRIGHTMOOR MACHINERY &nbsp;| &nbsp;All Rights Reserved</div>
    <div class="pay" style="left:860px">Paywell</div>
    <div class="pay" style="left:906px">Vantra</div>
    <div class="pay" style="left:952px">Cardmix</div>
    <div class="pay" style="left:998px">Amerpay</div>
    <div class="pay" style="left:1044px">Discova</div>
  </div>
</footer>

</body>
</html>
```